Vela Errands Web Design Project

Homepage components
o Logo
o Rotating header
o Main menu
o Animation video
o Banners
o Members login
o Latest news

The design’s preferred colors are black (background), silver (main tabs) and white (text)

Site map:
• Home
• News
• About us
o Welcome Note
o Company Profile
• Member Log in
o Registered homepage
? Request a service (form)
? Services directory
? Update profile
? Services history
• Member registration
o Registration form
• Partners
Footer Menu
• Contact us
• Terms & Conditions
• Privacy policy
• Social media links
• Sitemap

Brief about the company:
Vela Errands is a Jordanian company dedicated to elevate and redefine the level of service in the country. We are set out to give premium services at affordable prices. In this fast paced environment that we live in, we barely have the luxury of free time anymore and we, at Vela Errands will be giving you that extra hour or two per day to spend as your heart desires!
By becoming a member you will get access to a world of comfort and peace of mind. We have done the homework on your behalf and have established the network of connections that will enable you to live a headache free life.
We will be providing our members with support and assistance in their day to day lives in the fields that consumes and wastes time the most. We are value driven and below is our “ever-growing” list of services that we will provide at excellent prices:
• Maintenance (carpentry, plumbing, electrical, painting, decorating, gardening… etc)
• Cleaning (pre and post tenancy, periodical deep cleaning, packing and moving services, laundry… etc)
• Personalized delivery services (grocery, important documents, office related supplies, posting cheques, food, paying bills… etc)
• Passport, driving license and ID reissuance
• Travel arrangements (flights, hotels, airport transfers… etc)
• Premium car rental services
• Restaurant reservations
• IT assistance
• Event planning and all related services
• Catering arrangements

Aside from all the services we have on offer we have collaborated with a number of places (that we like to call partners) in town where Vela Errands members are entitled to benefits and privileges that will most certainly add value to their membership. Alongside our partners we have come up with the best formula that will please our members. Below are some of our current partners:

Requirements
Must have
• Homepage components
o Logo
o Rotating header
o Main menu
o Animation video
o Banners
o Members login
o Latest news

```html
<!DOCTYPE html>
<html lang="en">
<head>
<meta charset="utf-8">
<title>Vela Errands – Home</title>
<link rel="stylesheet" href="https://fonts.googleapis.com/css2?family=Crimson+Text:wght@400;600;700&family=Fjalla+One&family=Great+Vibes&display=swap">
<style>
:root{
  --paper:#ebe8dc;
  --ink:#252429;
  --ink-soft:#3a383d;
  --red:#a3161b;
  --red-dark:#7a0e12;
  --cream:#f3efe3;
  --white:#ffffff;
  --social:#3f78b8;
}
*{box-sizing:border-box;margin:0;padding:0}
html,body{width:1200px;height:938px;overflow:hidden}
body{background:radial-gradient(ellipse at 40% 30%,#f1efe6 0%,var(--paper) 60%,#e2dfd1 100%);font-family:"Crimson Text",Georgia,serif;color:var(--ink);position:relative}
.page{position:absolute;inset:0}
.brand{position:absolute;left:151px;top:14px;font-family:"Crimson Text",Georgia,serif;font-weight:600;font-size:26px;color:var(--ink);display:flex;align-items:center;gap:8px}
.brand-dot{width:10px;height:10px;border-radius:50%;background:var(--red)}
.login{position:absolute;left:480px;top:36px;width:325px;height:18px;background:var(--red);border:1px solid var(--ink);display:flex;align-items:center;font-size:12px;font-weight:700;color:var(--ink);padding:0 8px;gap:6px}
.login .field{width:74px;height:12px;background:var(--red-dark)}
.login .go{margin-left:auto}
.main-nav{position:absolute;left:155px;top:62px;display:flex;gap:14px;font-weight:700;font-size:20px;letter-spacing:-.2px}
.main-nav a{color:var(--ink);text-decoration:none}
.main-nav a.active{color:var(--red)}
.rule-thin{position:absolute;left:148px;top:103px;width:892px;height:5px;background:var(--ink)}
.rule-band{position:absolute;left:148px;top:112px;width:892px;height:14px;background:var(--ink)}
.hero-title{position:absolute;left:186px;top:150px;font-family:"Fjalla One","Oswald",sans-serif;font-size:44px;line-height:54px;color:var(--ink);text-transform:uppercase;letter-spacing:.5px}
.slide-dots{position:absolute;left:747px;top:344px;display:flex;gap:2px}
.slide-dots span{width:20px;height:20px;background:var(--red)}
.slide-dots span+span{background:#c0393d}
.hero-figure{position:absolute;left:808px;top:0;width:222px;height:440px;background:linear-gradient(180deg,#c42a2a 0%,#d8d6cc 22%,#d8d6cc 26%,#4a484a 40%,#5b595a 100%);border-radius:40% 40% 8px 8px / 18% 18% 2% 2%}
.band-dark{position:absolute;left:148px;top:375px;width:892px;height:22px;background:var(--ink)}
.feature{position:absolute;left:150px;top:415px;width:890px;height:212px;background:var(--ink)}
.feature p{position:absolute;left:38px;top:30px;width:245px;color:var(--white);font-size:16px;line-height:20.5px}
.video{position:absolute;left:379px;top:34px;width:446px;height:158px;border:3px solid var(--cream);background:linear-gradient(110deg,#4c5a2c 0%,#8a3d2a 35%,#c9b08a 65%,#a45046 100%)}
.video svg{position:absolute;left:198px;top:46px}
.col{position:absolute;top:632px}
.col h2{font-weight:600;font-size:25px;text-align:center;line-height:28px;margin-bottom:4px}
.welcome{left:184px;width:190px}
.welcome p{font-size:15px;line-height:17.5px}
.welcome a{display:block;margin:10px 0 0 14px;color:var(--red);font-size:17px;text-decoration:none}
.services{left:469px;width:230px}
.services h2{text-align:left;padding-left:20px}
.services ul{list-style:none;font-size:15px;line-height:17.2px}
.services li{position:relative;padding-left:28px}
.services li svg{position:absolute;left:0;top:0}
.news{left:765px;width:250px}
.news ul{list-style:none;margin-top:10px}
.news li{position:relative;padding-left:14px;font-size:15px;line-height:18px;margin-bottom:12px}
.news li::before{content:"";position:absolute;left:2px;top:6px;width:4px;height:4px;background:var(--red)}
.divider{position:absolute;top:650px;width:2px;height:200px;background:radial-gradient(circle,var(--ink) 1px,transparent 1.5px) 0 0/2px 17px repeat-y}
.footer{position:absolute;left:148px;top:884px;width:892px;height:54px;background:var(--ink);display:flex;align-items:center;padding-left:10px}
.footer nav{display:flex;gap:15px;font-weight:700;font-size:17px}
.footer a{color:var(--white);text-decoration:none}
.social{position:absolute;right:34px;top:14px;display:flex;gap:3px}
.social span{width:28px;height:28px;background:var(--social);border-radius:4px}
</style>
</head>
<body>
<div class="page">
  <div class="brand"><span class="brand-dot"></span>Vela Errands</div>

  <form class="login">
    <span>Name</span><span class="field"></span>
    <span>Password</span><span class="field"></span>
    <span class="go">Log in</span>
  </form>

  <nav class="main-nav">
    <a class="active" href="#">HOME</a>
    <a href="#">NEWS</a>
    <a href="#">ABOUT US</a>
    <a href="#">PARTNERS</a>
    <a href="#">CONTACT US</a>
    <a href="#">SERVICES</a>
    <a href="#">FAQS</a>
  </nav>

  <div class="rule-thin"></div>
  <div class="rule-band"></div>

  <h1 class="hero-title">Pleased to be one of<br>Jordan’s trusted companies<br>and happy to be at your<br>service.</h1>
  <div class="slide-dots"><span></span><span></span><span></span></div>

  <div class="band-dark"></div>
  <div class="hero-figure" role="img" aria-label="Illustration of a man in a suit whose head is a large grinning mouth"></div>

  <section class="feature">
    <p>Lorem ipsum dolor sit amet, consectetur adipisicing elit, sed do eiusmod tempor incididunt ut labore et dolore magna aliqua. Ut enim ad minim veniam, quis nostrud exercitation ullamco laboris nisi ut aliquip ex ea commodo consequat.</p>
    <div class="video" role="img" aria-label="Video still of a smiling couple shopping for flowers in a garden centre">
      <svg width="62" height="62" viewBox="0 0 62 62"><circle cx="31" cy="31" r="28" fill="rgba(40,40,40,.45)" stroke="#252429" stroke-width="3"/><path d="M24 17 L46 31 L24 45 Z" fill="#252429"/></svg>
    </div>
  </section>

  <section class="col welcome">
    <h2>Welcome</h2>
    <p>Lorem Ipsum is simply dummy text of the printing and typesetting industry. Lorem Ipsum has been the industry's standard dummy text ever since the 1500s, when an unknown printer took a galley of type and scrambled it to make a type specimen book. It has survived not only five centuries</p>
    <a href="#">Fnd out more</a>
  </section>

  <div class="divider" style="left:425px"></div>

  <section class="col services">
    <h2>Our Services</h2>
    <ul>
      <li><svg width="24" height="20" viewBox="0 0 24 20"><path d="M2 10 L9 17 L22 2 L9 12 Z" fill="#a3161b"/></svg>Maintenance</li>
      <li><svg width="24" height="20" viewBox="0 0 24 20"><path d="M2 10 L9 17 L22 2 L9 12 Z" fill="#a3161b"/></svg>Cleaning</li>
      <li><svg width="24" height="20" viewBox="0 0 24 20"><path d="M2 10 L9 17 L22 2 L9 12 Z" fill="#a3161b"/></svg>Personalized delivery services</li>
      <li><svg width="24" height="20" viewBox="0 0 24 20"><path d="M2 10 L9 17 L22 2 L9 12 Z" fill="#a3161b"/></svg>Passport, driving license and<br>ID reissuance</li>
      <li><svg width="24" height="20" viewBox="0 0 24 20"><path d="M2 10 L9 17 L22 2 L9 12 Z" fill="#a3161b"/></svg>Travel arrangements</li>
      <li><svg width="24" height="20" viewBox="0 0 24 20"><path d="M2 10 L9 17 L22 2 L9 12 Z" fill="#a3161b"/></svg>Premium car rental services</li>
      <li><svg width="24" height="20" viewBox="0 0 24 20"><path d="M2 10 L9 17 L22 2 L9 12 Z" fill="#a3161b"/></svg>Restaurant reservations</li>
      <li><svg width="24" height="20" viewBox="0 0 24 20"><path d="M2 10 L9 17 L22 2 L9 12 Z" fill="#a3161b"/></svg>IT assistance</li>
      <li><svg width="24" height="20" viewBox="0 0 24 20"><path d="M2 10 L9 17 L22 2 L9 12 Z" fill="#a3161b"/></svg>Event planning and<br>all related services</li>
      <li><svg width="24" height="20" viewBox="0 0 24 20"><path d="M2 10 L9 17 L22 2 L9 12 Z" fill="#a3161b"/></svg>Catering arrangements</li>
    </ul>
  </section>

  <div class="divider" style="left:736px"></div>

  <section class="col news">
    <h2>Latest News</h2>
    <ul>
      <li>Lorem Ipsum is simply dummy text of the printing and typesetting industry.</li>
      <li>Lorem Ipsum is simply dummy text of the printing and typesetting industry.</li>
      <li>Lorem Ipsum is simply dummy text of the printing and typesetting industry.</li>
      <li>Lorem Ipsum is simply dummy text of the printing and typesetting industry.</li>
    </ul>
  </section>

  <footer class="footer">
    <nav>
      <a href="#">PRIVACY POLICY</a>
      <a href="#">SITEMAP</a>
      <a href="#">PARTNERS</a>
      <a href="#">CONTACT US</a>
      <a href="#">TERMS AND CONDITIONS</a>
    </nav>
    <div class="social" aria-label="Social media links"><span></span><span></span><span></span></div>
  </footer>
</div>
</body>
</html>
```